Corvell Executive Search - New Business Card Design Project

We are an executive search firm called Corvell Executive Search based in the UK. We require a custom design for a business card. We're looking to convey a professional service to executives for executive search recruitment services. In terms of colours, we like dark blues and grays (maybe even silver incorporated somewhere if we go for a foiled type of card) but we're open to your artistic flare. See our current logo in attachments. We are totally open on design so long as the design is slick and professional.
Updates

Thanks for all your contributions of various designs. I have to say the quality of work has been amazing which is going to make our job quite difficult in the coming days on making a decision. Thanks to you all that have taken the time to submit designs thus far. We'll keep on reviewing and try to narrow down our selection as soon as possible.

Target Market(s)

Executive Search

Industry/Entity Type

Recruitment

Contact Information for Business Card

Corvell Executive Search,
Exclusively Sourcing & Hiring Senior Leaders
Dominic Haverley, Managing Director,
07742 318906
0117 468 2917
dominic@corvellexecutive.example
corvellexecutive.example
47 Linden Court, Marsh Lane, Bristol, BS9 7QT

Font styles to use
Sans Serif
Other font styles liked:
• Roboto (which is used in our logo)

Requirements
Must have
• Our logo (It has a subtle fade on it from #02071d at top to #333649 at bottom)
• The logo can be on one side or both sides
• Must be elegant and professional
• We have 2nd slogan CONSULT | INSPIRE | INNOVATE | DELIVER which can be incorporated into the card
Nice to have
• Use of blues and grey colours
• Compatible with similar styling to our website corvellexecutive.example
Should not have
• Must not be overly brash
• Must not contain cartoon characters

```html
<!DOCTYPE html>
<html lang="en">
<head>
<meta charset="utf-8">
<title>Corvell Executive Search – Business Card</title>
<link href="https://fonts.googleapis.com/css2?family=Roboto:wght@300;400;500;700&display=swap" rel="stylesheet">
<style>
  :root {
    --page-bg: #1c1d21;
    --card-top: #0d1226;
    --card-bottom: #343a52;
    --silver: #b8bcc6;
    --white: #f4f5f8;
    --grey: #9a9eab;
    --accent: #4a9fe0;
    --rule: #c9ccd4;
  }
  * { box-sizing: border-box; margin: 0; padding: 0; }
  html, body {
    width: 1200px; height: 1200px; overflow: hidden;
    background: var(--page-bg);
    font-family: "Roboto", Arial, sans-serif;
  }
  .canvas {
    width: 1200px; height: 1200px;
    display: flex; flex-direction: column; align-items: center; justify-content: center;
    gap: 60px;
  }
  .card {
    position: relative;
    width: 880px; height: 500px;
    background: linear-gradient(180deg, var(--card-top) 0%, var(--card-bottom) 100%);
    box-shadow: 0 14px 30px rgba(0,0,0,.55);
    overflow: hidden;
  }
  .wordmark { color: var(--silver); font-weight: 500; line-height: 1; }
  .wordmark__name { display: block; letter-spacing: 2px; }
  .wordmark__sub { display: block; letter-spacing: 1px; }

  /* Front */
  .card--front .wordmark { position: absolute; left: 110px; top: 215px; }
  .card--front .wordmark__name { font-size: 78px; }
  .card--front .wordmark__sub { font-size: 44px; margin-top: 4px; }
  .card--front .tagline {
    position: absolute; left: 112px; top: 335px;
    font-size: 20px; font-weight: 400; color: var(--grey); letter-spacing: .6px;
  }

  /* Back */
  .card--back .wordmark { position: absolute; left: 60px; top: 55px; color: var(--white); }
  .card--back .wordmark__name { font-size: 56px; }
  .card--back .wordmark__sub { font-size: 34px; margin-top: 2px; }
  .slogan {
    position: absolute; left: 60px; top: 150px;
    font-size: 20px; color: var(--accent); letter-spacing: .8px;
    display: flex; gap: 12px; align-items: center;
  }
  .slogan__dot { width: 6px; height: 6px; border-radius: 50%; background: var(--grey); }
  .person { position: absolute; right: 70px; top: 95px; text-align: right; width: 330px; }
  .person__name { font-size: 24px; font-weight: 700; color: var(--white); letter-spacing: 1.2px; }
  .person__role { font-size: 20px; color: var(--grey); margin-top: 6px; letter-spacing: .8px; }
  .person__rule { height: 4px; background: var(--accent); margin-top: 12px; }
  .divider { position: absolute; left: 60px; right: 100px; top: 320px; height: 1.5px; background: var(--rule); }
  .contacts { position: absolute; left: 60px; top: 345px; list-style: none; }
  .contacts li {
    display: flex; align-items: center; gap: 12px;
    font-size: 21px; color: var(--white); letter-spacing: .4px; height: 30px;
  }
  .contacts svg { width: 20px; height: 20px; flex: none; }
  .address {
    position: absolute; right: 100px; top: 350px; text-align: right;
    font-size: 21px; color: var(--white); line-height: 1.45; letter-spacing: .4px; font-style: normal;
  }
</style>
</head>
<body>
<main class="canvas">
  <section class="card card--front" aria-label="Card front">
    <div class="wordmark">
      <span class="wordmark__name">CORVELL</span>
      <span class="wordmark__sub">EXECUTIVE SEARCH</span>
    </div>
    <p class="tagline">Exclusively Sourcing &amp; Hiring Senior Leaders</p>
  </section>

  <section class="card card--back" aria-label="Card back">
    <div class="wordmark">
      <span class="wordmark__name">CORVELL</span>
      <span class="wordmark__sub">EXECUTIVE SEARCH</span>
    </div>
    <p class="slogan">
      <span>Consult</span><span class="slogan__dot"></span>
      <span>Inspire</span><span class="slogan__dot"></span>
      <span>Innovate</span><span class="slogan__dot"></span>
      <span>Deliver</span>
    </p>

    <div class="person">
      <p class="person__name">DOMINIC HAVERLEY</p>
      <p class="person__role">Managing Director</p>
      <div class="person__rule"></div>
    </div>

    <div class="divider"></div>

    <ul class="contacts">
      <li>
        <svg viewBox="0 0 20 20" fill="none" stroke="var(--accent)" stroke-width="2"><rect x="3" y="3" width="14" height="12" rx="2"/><line x1="8" y1="18" x2="12" y2="18"/></svg>
        07742 318906
      </li>
      <li>
        <svg viewBox="0 0 20 20" fill="var(--accent)"><path d="M2 7c0-2 3-4 8-4s8 2 8 4v2h-4V7.5c-1-.6-2.5-.9-4-.9s-3 .3-4 .9V9H2z"/><rect x="4" y="11" width="12" height="6" rx="1"/></svg>
        0117 468 2917
      </li>
      <li>
        <svg viewBox="0 0 20 20" fill="none" stroke="var(--accent)" stroke-width="2"><rect x="2" y="4" width="16" height="12"/><polyline points="2,4 10,11 18,4"/></svg>
        dominic@corvellexecutive.example
      </li>
      <li>
        <svg viewBox="0 0 20 20" fill="none" stroke="var(--accent)" stroke-width="1.6"><circle cx="10" cy="10" r="8"/><ellipse cx="10" cy="10" rx="3.5" ry="8"/><line x1="2" y1="10" x2="18" y2="10"/></svg>
        corvellexecutive.example
      </li>
    </ul>

    <address class="address">
      47 Linden Court, Marsh Lane<br>
      Bristol, BS9 7QT
    </address>
  </section>
</main>
</body>
</html>
```